Ferrando Quispe Law Firm for Small and Medium Business: Website

We need a web design that includes coding for the Wix platform, for a new company based in Santiago, Chile, called Ferrando Quispe, Abogados y Consultores. The company is essentially a law firm, with additional advisory services in accounting, tax management and finance. The main target of the company are founders, CEOs or C-level executives of small or medium companies based in Chile.
The main menu of the web page must have the following tab options:
- Home - About us - Services – How we work -Blog – FAQ -Contact
Our main services are:

1.- Commercial and corporate law advisory
2.- Legal defense in civil, criminal, labor and family matters (litigation and arbitration)
3.- Bankruptcy and reorganization of companies
4.- Collection and recovery of assets
5.- Asset protection
6.- Financial and tax advice

We want to highlight the following services:

-Bankruptcy and reorganization of companies
-Judicial defense in civil matters
-Financial and tax advice

In addition to these services, the following will be offered:
-Lawyer at your home for special cases
-Half hour free consultation
-Monthly service packages

The final design should communicate confidence, business savvy and high execution standards and quality.

Target Market(s)

The main target of the company are founders, CEOs or C-level executives of small or medium companies based in Chile.

Industry/Entity Type

Legal industry

Coding

Coded - Design and coding required

Number of Pages Required

5+ page

Font styles to use
Serif

Requirements
Must have
• 1. Big banners para destacar los siguientes servicios: -Bankruptcy and reorganization of companies -Judicial defense in civil matters -Financial and tax advice 2. Call to action para agendar consulta legal. 3. Destacar los siguientes servicios: -Lawyer at your home for special cases -Half hour free consultation -Monthly service packages 3. Página para explicar cómo se cobra (precios transparentes): ver el siguiente sitio web: https://www.brindlemoorlegal.example/how 4. Links to Facebook, Instagram and Linkedin 5. Connection to Whatsapp.
Should not have
• Look old fashioned

```html
<!DOCTYPE html>
<html lang="en">
<head>
<meta charset="utf-8">
<title>Ferrando Quispe Law Firm</title>
<link href="https://fonts.googleapis.com/css2?family=EB+Garamond:wght@400;500;600&family=Poppins:wght@400;500;600&display=swap" rel="stylesheet">
<style>
:root{
  --green-deep:#1b3128;
  --green-dark:#1f3a2e;
  --green-card:#164a36;
  --green-card-alt:#123d2c;
  --gold:#c8ad4a;
  --gold-light:#e4d07c;
  --gold-grad:linear-gradient(90deg,#a8862a,#d8c06a 55%,#b8963a);
  --gray-bg:#efefef;
  --white:#ffffff;
  --ink:#222;
  --faq-gray:#7e938a;
}
*{box-sizing:border-box;margin:0;padding:0}
html,body{width:1200px;height:3000px;overflow:hidden;background:#f4f4f2}
body{font-family:"Poppins",sans-serif;color:var(--ink)}
.page{position:absolute;left:200px;top:0;width:800px;height:3000px;background:var(--white);overflow:hidden}
.serif{font-family:"EB Garamond",serif}
.abs{position:absolute}
.btn{position:absolute;background:var(--gold-grad);color:#fff;font-family:"Poppins",sans-serif;font-weight:600;text-transform:uppercase;text-align:center;border-radius:2px;letter-spacing:.3px}

/* header */
.topbar{top:0;left:0;width:800px;height:42px;background:var(--green-deep)}
.brand{display:flex;align-items:center;gap:5px;font-family:"EB Garamond",serif;color:var(--gold)}
.brand-square{width:18px;height:18px;background:var(--gold)}
.brand-name{font-size:15px;line-height:1}
.brand-sub{font-size:4.5px;letter-spacing:.4px;text-transform:uppercase;color:var(--gold);font-family:"Poppins",sans-serif}
.hours{right:36px;top:8px;color:#fff;text-align:right}
.hours-time{font-size:12px;font-weight:500;display:flex;align-items:center;justify-content:flex-end;gap:8px}
.hours-note{font-size:7px;margin-top:2px}
.navbar{top:42px;left:0;width:800px;height:34px;background:var(--green-deep);border-top:1px solid #2e4a3e}
.nav{position:absolute;left:49px;top:11px;display:flex;font-size:9px;color:#fff}
.nav span{margin-right:38px}
.nav .active{color:var(--gold-light)}
.nav-cta{right:57px;top:8px;width:72px;height:18px;font-size:7.5px;line-height:18px}

/* hero + about */
.dark-block{top:76px;left:0;width:800px;height:695px;background:var(--green-deep)}
.hero-photo{top:76px;left:0;width:800px;height:370px;background:linear-gradient(180deg,#3c6f78 0%,#2f5c63 45%,#24453f 78%,var(--green-deep) 100%)}
.hero-title{top:252px;left:0;width:800px;text-align:center;font-size:50px;color:var(--gold-light);font-weight:500}
.hero-btn{left:345px;top:324px;width:112px;height:27px;font-size:10px;line-height:27px}
.about-title{top:520px;left:81px;font-size:38px;color:var(--gold-light)}
.about-title::after{content:"";position:absolute;left:0;bottom:2px;width:145px;height:2px;background:var(--gold)}
.about-text{top:587px;left:81px;width:318px;font-size:9px;line-height:14.4px;color:#fff}
.about-btn{left:81px;top:696px;width:82px;height:20px;font-size:7px;line-height:20px}
.emblem{top:514px;left:498px;width:203px;height:203px;border-radius:10px;background:linear-gradient(135deg,#a8862a,#e8d585 50%,#a38126)}

/* section titles */
.sec-title{position:absolute;left:0;width:800px;text-align:center;font-family:"EB Garamond",serif;color:var(--gold);font-size:38px;font-weight:500}
.rule{position:absolute;left:352px;width:96px;height:3px;background:linear-gradient(90deg,var(--green-card) 50%,var(--gold) 50%)}

/* how we work */
.how-intro{top:916px;left:150px;width:500px;text-align:center;font-size:9px;line-height:14px;color:#222}
.step{position:absolute;left:84px;display:flex;gap:14px}
.step-num{width:45px;height:45px;border-radius:50%;background:var(--gold);color:#fff;font-weight:600;font-size:18px;display:flex;align-items:center;justify-content:center;flex:none}
.step h4{font-family:"EB Garamond",serif;font-size:12.5px;font-weight:600;color:#111;margin-bottom:3px}
.step p{font-size:8.8px;line-height:14px;color:#222;width:285px}
.how-frame{top:993px;left:477px;width:230px;height:216px;border-left:5px solid var(--green-card);border-bottom:5px solid var(--green-card)}
.how-photo{top:968px;left:488px;width:244px;height:228px;background:linear-gradient(135deg,#4d5a60,#7d8d92 55%,#bfc7c6)}

/* services */
.services-band{top:1293px;left:0;width:800px;height:169px;background:linear-gradient(90deg,#1d4a38,#234f3e 50%,#1a4434)}
.services-gray{top:1462px;left:0;width:800px;height:224px;background:var(--gray-bg)}
.cards{top:1420px;left:78px;width:642px;height:200px;display:flex}
.card{flex:1;background:var(--green-card);padding:20px 10px 0;text-align:center;position:relative;color:#fff}
.card.alt{background:var(--green-card-alt)}
.card h5{font-family:"EB Garamond",serif;color:var(--gold-light);font-size:10.5px;font-weight:600;line-height:12px;margin:10px 0 5px}
.card p{font-size:8px;line-height:12.6px}
.card .more{position:absolute;right:14px;bottom:9px;font-size:8px;font-weight:500}
.arrows{top:1643px;left:676px;display:flex;gap:16px}

/* blog */
.blog-big-img{top:1848px;left:42px;width:307px;height:215px;background:linear-gradient(135deg,#465359,#8a979a 55%,#c9cfcc)}
.label{position:absolute;background:var(--green-card);color:#fff;font-family:"EB Garamond",serif;font-size:10.5px;padding-left:6px;display:flex;align-items:center}
.blog-text{position:absolute;font-size:8px;line-height:12.6px;color:#333}
.blog-img{position:absolute;width:180px;height:78px}
.img-a{background:linear-gradient(135deg,#4d5a60,#8d9a9d 60%,#c5cbc9)}
.img-b{background:linear-gradient(135deg,#2c3848,#6a7688 55%,#d9dde0)}
.blog-btn{left:352px;top:2207px;width:96px;height:20px;font-size:7.5px;line-height:20px}

/* faq */
.faq-bg{top:2284px;left:0;width:800px;height:455px;background:var(--gray-bg)}
.faq{position:absolute;left:137px;width:526px;border-radius:7px;background:var(--faq-gray);color:#fff;font-size:10.5px;display:flex;align-items:center;padding:0 18px 0 12px}
.faq .n{width:18px;height:18px;border:1px solid #fff;border-radius:50%;font-size:9px;display:flex;align-items:center;justify-content:center;margin-right:19px;flex:none}
.faq .q{flex:1}
.faq.open{background:var(--green-card);align-items:flex-start;padding-top:11px;line-height:15px}
.faq-btn{left:352px;top:2673px;width:96px;height:20px;font-size:7.5px;line-height:20px}

/* footer */
.footer{top:2739px;left:0;width:800px;height:261px;background:var(--green-deep);color:#fff}
.foot-h{position:absolute;font-family:"EB Garamond",serif;font-size:15px;letter-spacing:.4px}
.foot-links{position:absolute;font-family:"EB Garamond",serif;font-size:11.5px;line-height:14px}
.foot-links .active{color:var(--gold-light)}
.contact-row{position:absolute;left:355px;display:flex;gap:10px;font-family:"EB Garamond",serif;font-size:10.5px;line-height:13px}
.field{position:absolute;background:#fff;color:#999;font-size:7.5px;padding:3px 6px;border:1px solid #ccc}
.foot-tag{position:absolute;left:36px;top:119px;width:135px;font-family:"EB Garamond",serif;font-size:8px;line-height:10px}
.copyright{position:absolute;left:0;top:244px;width:800px;text-align:center;font-size:7px}
.foot-line{position:absolute;left:97px;top:237px;width:606px;height:1px;background:#6c7d74}
</style>
</head>
<body>
<div class="page">

  <header>
    <div class="abs topbar">
      <div class="abs brand" style="left:49px;top:12px">
        <div class="brand-square"></div>
        <div>
          <div class="brand-name">Ferrando Quispe</div>
          <div class="brand-sub">Abogados y Consultores</div>
        </div>
      </div>
      <div class="abs hours">
        <div class="hours-time">
          <svg width="18" height="18" viewBox="0 0 18 18"><circle cx="9" cy="9" r="7.5" fill="none" stroke="#c8ad4a" stroke-width="1.5"/><path d="M9 4.5V9h3.5" fill="none" stroke="#c8ad4a" stroke-width="1.5"/></svg>
          8.00 - 9.00
        </div>
        <div class="hours-note">Our Opening Hours Mon To Fri</div>
      </div>
    </div>
    <nav class="abs navbar">
      <div class="nav">
        <span class="active">Home</span><span>About us</span><span>Services</span><span>How we work</span><span>Blog</span><span>FAQ</span>
      </div>
      <div class="btn nav-cta">Contact us</div>
    </nav>
  </header>

  <section class="hero-about">
    <div class="abs dark-block"></div>
    <div class="abs hero-photo" role="img" aria-label="Photo of two lawyers in a meeting at an office desk"></div>
    <h1 class="abs hero-title serif">Ferrando Quispe Law Firm</h1>
    <div class="btn hero-btn">Get started</div>

    <h2 class="abs about-title serif">About Us</h2>
    <p class="abs about-text">Lorem Ipsum Dolor Sit Amet, Consectetur Adipiscing Elit. In Tellus Id Auctor Molestie Vel Orci Faucibus Mauris. Scelerisque Elementum Condimentum Sollicitudin Duis Morbi Sem Ut Fringilla. Mollis Neque Et, Morbi Et Lectus. Dolor Eget Habitasse Mattis Ornare Imperdiet Pellentesque Bibendum. Arcu, Mattis Ornare Imperdiet Pellentesque Bibendum. Arcu, Mattis Ornare Imperdiet Pellentesque Bibendum. Arcu,</p>
    <div class="btn about-btn">Learn more</div>
    <div class="abs emblem" role="img" aria-label="Gold brand panel"></div>
  </section>

  <section class="how">
    <h2 class="sec-title" style="top:839px">How We Work</h2>
    <div class="rule" style="top:897px"></div>
    <p class="abs how-intro">Lorem Ipsum Dolor Sit Amet, Consectetur Adipiscing Elit. In Tellus Id Auctor Molestie Vel Orci Faucibus Mauris. Scelerisque Elementum Condimentum Sollicitudin</p>

    <div class="step" style="top:1001px"><div class="step-num">01</div><div><h4>Lorem Ipsum Dolor</h4><p>Lorem Ipsum Dolor Sit Amet, Consectetur Adipiscing Elit. In Tellus Id Auctor Molestie Vel Orci Faucibus Mauris.</p></div></div>
    <div class="step" style="top:1072px"><div class="step-num">02</div><div><h4>Lorem Ipsum Dolor</h4><p>Lorem Ipsum Dolor Sit Amet, Consectetur Adipiscing Elit. In Tellus Id Auctor Molestie Vel Orci Faucibus Mauris.</p></div></div>
    <div class="step" style="top:1143px"><div class="step-num">03</div><div><h4>Lorem Ipsum Dolor</h4><p>Lorem Ipsum Dolor Sit Amet, Consectetur Adipiscing Elit. In Tellus Id Auctor Molestie Vel Orci Faucibus Mauris.</p></div></div>

    <div class="abs how-frame"></div>
    <div class="abs how-photo" role="img" aria-label="Photo of three colleagues reviewing work on a laptop"></div>
  </section>

  <section class="services">
    <div class="abs services-band" role="img" aria-label="Dark green tinted photo of a business desk"></div>
    <div class="abs services-gray"></div>
    <h2 class="sec-title" style="top:1337px;color:var(--gold-light)">Our Services</h2>
    <div class="rule" style="top:1388px;background:linear-gradient(90deg,#fff 50%,var(--gold) 50%)"></div>
    <div class="abs cards">
      <div class="card">
        <svg width="44" height="36" viewBox="0 0 44 36" fill="none" stroke="#c8ad4a" stroke-width="1.6"><path d="M22 3v29M10 32h24M6 8h32M6 8l-5 13h10zM38 8l-5 13h10zM1 21a5 3 0 0 0 10 0M33 21a5 3 0 0 0 10 0"/></svg>
        <h5>Bankruptcy And Reorganization Of Companies</h5>
        <p>Lorem Ipsum Dolor Sit Amet, Consectetur Adipiscing Elit. In Tellus Id Auctor Molestie Vel Orci Faucibus Mauris. Vel Orci Faucibus Mauris.</p>
        <span class="more">Read More</span>
      </div>
      <div class="card alt">
        <svg width="44" height="36" viewBox="0 0 44 36" fill="none" stroke="#c8ad4a" stroke-width="1.6"><path d="M22 3v29M10 32h24M6 8h32M6 8l-5 13h10zM38 8l-5 13h10zM1 21a5 3 0 0 0 10 0M33 21a5 3 0 0 0 10 0"/></svg>
        <h5>Judicial Defense In Civil Matters</h5>
        <p>Lorem Ipsum Dolor Sit Amet, Consectetur Adipiscing Elit. In Tellus Id Auctor Molestie Vel Orci Faucibus Mauris. Vel Orci Faucibus Mauris.</p>
        <span class="more">Read More</span>
      </div>
      <div class="card">
        <svg width="44" height="36" viewBox="0 0 44 36" fill="none" stroke="#c8ad4a" stroke-width="1.6"><path d="M22 3v29M10 32h24M6 8h32M6 8l-5 13h10zM38 8l-5 13h10zM1 21a5 3 0 0 0 10 0M33 21a5 3 0 0 0 10 0"/></svg>
        <h5>Financial And Tax Advice</h5>
        <p>Lorem Ipsum Dolor Sit Amet, Consectetur Adipiscing Elit. In Tellus Id Auctor Molestie Vel Orci Faucibus Mauris. Vel Orci Faucibus Mauris.</p>
        <span class="more">Read More</span>
      </div>
      <div class="card alt">
        <svg width="44" height="36" viewBox="0 0 44 36" fill="none" stroke="#c8ad4a" stroke-width="1.6"><path d="M22 3v29M10 32h24M6 8h32M6 8l-5 13h10zM38 8l-5 13h10zM1 21a5 3 0 0 0 10 0M33 21a5 3 0 0 0 10 0"/></svg>
        <h5>Lawyer At Your Home For Special Cases</h5>
        <p>Lorem Ipsum Dolor Sit Amet, Consectetur Adipiscing Elit. In Tellus Id Auctor Molestie Vel Orci Faucibus Mauris. Vel Orci Faucibus Mauris.</p>
        <span class="more">Read More</span>
      </div>
    </div>
    <div class="abs arrows">
      <svg width="28" height="20" viewBox="0 0 28 20" fill="none" stroke="#8a6d1c" stroke-width="1.5"><path d="M27 10H2M9 3l-7 7 7 7"/></svg>
      <svg width="28" height="20" viewBox="0 0 28 20" fill="none" stroke="#1b3128" stroke-width="1.5"><path d="M1 10h25M19 3l7 7-7 7"/></svg>
    </div>
  </section>

  <section class="blog">
    <h2 class="sec-title" style="top:1746px;font-size:44px">Blogs/News</h2>
    <div class="rule" style="top:1810px"></div>

    <div class="abs blog-big-img" role="img" aria-label="Photo of colleagues working together at a laptop"></div>
    <div class="label" style="left:42px;top:2063px;width:307px;height:25px;padding-left:16px">LOREM IPSUM</div>
    <p class="blog-text" style="left:42px;top:2103px;width:305px">lorem ipsum dolor sit amet, consectetur adipiscing elit. dui sit lacinia sed lacus. proin adipiscing nibh eget eget. egestas lacus, eros, massa, volutpat sit velit platea nisl.lorem ipsum dolor sit amet, consectetur adipiscing elit. dui sit lacinia sed lacus. proin adipiscing nibh eget eget. egestas lacus, eros, massa, volutpat sit velit platea nisl.</p>

    <div class="blog-img img-a" style="left:367px;top:1848px" role="img" aria-label="Photo of colleagues at a laptop"></div>
    <div class="label" style="left:367px;top:1926px;width:180px;height:21px">LOREM IPSUM</div>
    <p class="blog-text" style="left:369px;top:1959px;width:176px">lorem ipsum dolor sit amet, consectetur adipiscing elit. fermentum pharetra quis viverra donec magna lacus. felis amet,</p>

    <div class="blog-img img-b" style="left:562px;top:1848px" role="img" aria-label="Photo of hands signing a document"></div>
    <div class="label" style="left:562px;top:1926px;width:180px;height:21px">LOREM IPSUM</div>
    <p class="blog-text" style="left:564px;top:1959px;width:176px">lorem ipsum dolor sit amet, consectetur adipiscing elit. fermentum pharetra quis viverra donec magna lacus. felis amet,</p>

    <div class="blog-img img-b" style="left:367px;top:2008px" role="img" aria-label="Photo of hands signing a document"></div>
    <div class="label" style="left:367px;top:2086px;width:180px;height:21px">LOREM IPSUM</div>
    <p class="blog-text" style="left:369px;top:2119px;width:176px">lorem ipsum dolor sit amet, consectetur adipiscing elit. fermentum pharetra quis viverra donec magna lacus. felis amet,</p>

    <div class="blog-img img-a" style="left:562px;top:2008px" role="img" aria-label="Photo of colleagues at a laptop"></div>
    <div class="label" style="left:562px;top:2086px;width:180px;height:21px">LOREM IPSUM</div>
    <p class="blog-text" style="left:564px;top:2119px;width:176px">lorem ipsum dolor sit amet, consectetur adipiscing elit. fermentum pharetra quis viverra donec magna lacus. felis amet,</p>

    <div class="btn blog-btn">View more</div>
  </section>

  <section class="faq-section">
    <div class="abs faq-bg"></div>
    <h2 class="sec-title" style="top:2307px">Frequently Asked Questions</h2>
    <div class="rule" style="left:290px;width:220px;top:2365px"></div>

    <div class="faq" style="top:2399px;height:33px"><span class="n">01</span><span class="q">Lorem Ipsum Dolor Sit Amet, Consectetur Adipiscing Ipsum Dolor Sit Amet ?</span><span>+</span></div>
    <div class="faq open" style="top:2450px;height:81px"><span class="n">01</span><span class="q">Lorem Ipsum Dolor, Consectetur Adipiscing Ipsum Dolor Sit Amet Lorem Ipsumsit Amet, Cur Adipiscing Ipsum Dolor Sit Amet Lorem Ipsum Dolor Sit Amet, Consectetur Adipiscinpsum R Sit Amet</span><span>&minus;</span></div>
    <div class="faq" style="top:2549px;height:33px"><span class="n">02</span><span class="q">Lorem Ipsum Dolor Sit Amet, Consectetur Adipiscing Ipsum Dolor Sit Amet ?</span><span>+</span></div>
    <div class="faq" style="top:2601px;height:33px"><span class="n">03</span><span class="q">Lorem Ipsum Dolor Sit Amet, Consectetur Adipiscing Ipsum Dolor Sit Amet ?</span><span>+</span></div>

    <div class="btn faq-btn">View more</div>
  </section>

  <footer class="abs footer">
    <div class="abs brand" style="left:36px;top:86px">
      <div class="brand-square" style="width:24px;height:24px"></div>
      <div>
        <div class="brand-name" style="font-size:19px">Ferrando Quispe</div>
        <div class="brand-sub" style="font-size:5px">Abogados y Consultores</div>
      </div>
    </div>
    <p class="foot-tag">As You Can See, There Are Plenty Of Reasons To Consider Collaborative Practice.</p>

    <div class="foot-h" style="left:215px;top:50px">QUICK LINKS</div>
    <div class="foot-links" style="left:219px;top:76px">
      <div class="active">Home</div><div>About Us</div><div>Services</div><div>How We</div><div>Work</div><div>Blog</div><div>FAQ</div>
    </div>

    <div class="foot-h" style="left:355px;top:50px">CONTACT US</div>
    <div class="contact-row" style="top:78px">
      <svg width="12" height="12" viewBox="0 0 12 12"><path d="M3 1l2 2.5-1.2 1.3a7 7 0 0 0 3.4 3.4L8.5 7 11 9l-1 2C5 11 1 7 1 2z" fill="#c8ad4a"/></svg>
      <span>5550-1212-34</span>
    </div>
    <div class="contact-row" style="top:99px">
      <svg width="12" height="12" viewBox="0 0 12 12" fill="none" stroke="#c8ad4a"><rect x="1" y="2.5" width="10" height="7"/><path d="M1 2.5l5 4 5-4"/></svg>
      <span>hello@ferrandoquispe.example</span>
    </div>
    <div class="contact-row" style="top:122px">
      <svg width="12" height="12" viewBox="0 0 12 12"><path d="M11 1L1 5.5l4.5 1 1 4.5z" fill="#c8ad4a"/></svg>
      <span>Street no 4 near plaza ,<br>Santiago Chile</span>
    </div>

    <div class="foot-h" style="left:532px;top:45px">GET IN TOUCH</div>
    <div class="field" style="left:532px;top:78px;width:106px;height:18px">Name</div>
    <div class="field" style="left:650px;top:78px;width:106px;height:18px">Phone number</div>
    <div class="field" style="left:532px;top:104px;width:106px;height:18px">Subject</div>
    <div class="field" style="left:650px;top:104px;width:106px;height:18px">Email</div>
    <div class="field" style="left:532px;top:130px;width:224px;height:40px">Message</div>
    <div class="btn" style="left:532px;top:182px;width:76px;height:19px;font-size:7.5px;line-height:19px">Submit</div>

    <div class="foot-line"></div>
    <p class="copyright">COPYRIGHTS © 2021 FERRANDO QUISPE LAW. ALL RIGHTS RESERVED. TERMS &amp; CONDITIONS</p>
  </footer>

</div>
</body>
</html>
```